Business Card Design Project

Hello- I am an interior stylist/product designer whose work is detail driven, very clean and transitional in style and I want my business card to reflect those qualities. I have a logo that I use on my website- my name and a hand drawn chandelier that I want incorporated into the design. However, "Design for the Home" needs to be changed to "Designs". I will be using cream colored stock and am thinking of gray text and logo. I need your help in pulling my card together since it will be the most used element and drive the design of the rest of my stationary suite.
Updates

Please note that I have changed my QR code from my cell # to my website. The new code will be downloaded now.

Reason: I want to thank everyone who has submitted designs- there are truly some very inspiring designs and I am very pleased. I want to make certain that I get this right and have an attractive and highly effective marketing tool when we are finished. With that said, I have run into a technical problem with one aspect of the card- a qr code for my website that was not part of the original brief. I will get that corrected today and post. Once I get that taken care of, I will post comments to all designs received do far. Thanks again for everyone's efforts, Risa

QR Code for the website is now uploaded. Thanks for your patience!

Target Market(s)

Upper middle class- mostly women

Industry/Entity Type

Business

Requirements
Must have
• Marisa Vantry Designs
"...to the last detail."
214-555-0148
marisavantry@plumwick.net
www.marisavantrydesigns-example.com
27083 Birchmont Court
Dallas, TX 75000
Nice to have
• Risa Vantry
Owner

```html
<!DOCTYPE html>
<html lang="en">
<head>
<meta charset="utf-8">
<title>Marisa Vantry Designs — Business Card</title>
<link rel="stylesheet" href="https://fonts.googleapis.com/css2?family=Questrial&family=Sorts+Mill+Goudy&display=swap">
<style>
  :root {
    --page: #ffffff;
    --stock: #fef9dc;
    --ink: #3b3b38;
    --logo-ink: #4a5b5c;
    --logo-accent: #86a6ae;
    --sconce-light: #e3ebe9;
    --sconce-mid: #c3d3d5;
  }
  * { margin: 0; padding: 0; box-sizing: border-box; }
  html, body {
    width: 999px;
    height: 1200px;
    overflow: hidden;
    background: var(--page);
  }
  .sheet {
    position: relative;
    width: 999px;
    height: 1200px;
    font-family: "Sorts Mill Goudy", "Goudy Old Style", Georgia, serif;
    color: var(--ink);
  }
  .card {
    position: absolute;
    left: 58px;
    width: 908px;
    height: 534px;
    background: var(--stock);
    overflow: hidden;
  }
  .card--front { top: 54px; }
  .card--back { top: 621px; }

  /* Front: name lockup */
  .lockup {
    position: absolute;
    left: 0;
    right: 0;
    top: 222px;
    height: 184px;
    display: flex;
    justify-content: center;
    align-items: flex-end;
    gap: 26px;
  }
  .brand-word {
    font-size: 72px;
    line-height: 0.86;
    color: var(--logo-ink);
    letter-spacing: 0.5px;
  }
  .brand-mark {
    width: 120px;
    height: 150px;
    background: var(--sconce-mid);
    opacity: 0.6;
    flex: none;
  }
  .brand-line {
    position: absolute;
    left: 0;
    right: 0;
    top: 418px;
    text-align: center;
    font-family: "Questrial", Arial, sans-serif;
    font-size: 21px;
    line-height: 1;
    letter-spacing: 4.2px;
    color: var(--logo-accent);
  }

  /* Back */
  .sconce {
    position: absolute;
    width: 190px;
  }
  .sconce--left { left: 0; top: 168px; height: 288px; }
  .sconce--right { right: 0; top: 94px; height: 158px; }

  .studio-name {
    position: absolute;
    left: 69px;
    top: 78px;
    font-size: 41px;
    font-weight: 400;
    line-height: 1;
    letter-spacing: 0.5px;
  }
  .tagline {
    position: absolute;
    left: 0;
    width: 467px;
    top: 130px;
    text-align: right;
    font-size: 24px;
    line-height: 1;
    letter-spacing: 0.6px;
  }

  .contact {
    position: absolute;
    left: 470px;
    top: 282px;
    list-style: none;
    font-size: 21px;
    line-height: 1;
    letter-spacing: 0.2px;
    white-space: nowrap;
  }
  .contact li { height: 36px; }
  .contact .addr { font-size: 24px; height: 33px; }
  .contact .addr + .addr { height: 38px; }
</style>
</head>
<body>
<main class="sheet">

  <section class="card card--front" aria-label="Card front">
    <div class="lockup">
      <span class="brand-word">Marisa</span>
      <span class="brand-mark" role="img" aria-label="Place for the studio mark"></span>
      <span class="brand-word">Vantry</span>
    </div>
    <p class="brand-line">DESIGNS FOR THE HOME</p>
  </section>

  <section class="card card--back" aria-label="Card back">
    <svg class="sconce sconce--left" role="img" aria-label="Hand-drawn wrought iron wall sconce with shaded lamps" viewBox="0 0 190 288" preserveAspectRatio="none">
      <defs>
        <linearGradient id="sconceLeftTone" x1="0" y1="0" x2="1" y2="1">
          <stop offset="0" stop-color="var(--sconce-mid)"/>
          <stop offset="1" stop-color="var(--sconce-light)"/>
        </linearGradient>
      </defs>
      <rect width="190" height="288" fill="url(#sconceLeftTone)" opacity="0.7"/>
    </svg>

    <svg class="sconce sconce--right" role="img" aria-label="Hand-drawn wrought iron wall sconce with shaded lamps" viewBox="0 0 190 158" preserveAspectRatio="none">
      <defs>
        <linearGradient id="sconceRightTone" x1="1" y1="0" x2="0" y2="1">
          <stop offset="0" stop-color="var(--sconce-mid)"/>
          <stop offset="1" stop-color="var(--sconce-light)"/>
        </linearGradient>
      </defs>
      <rect width="190" height="158" fill="url(#sconceRightTone)" opacity="0.7"/>
    </svg>

    <h1 class="studio-name">Marisa Vantry Designs</h1>
    <p class="tagline">…to the last detail</p>

    <ul class="contact">
      <li>214-555-0148</li>
      <li class="addr">27083 Birchmont Court</li>
      <li class="addr">Dallas, TX 75000</li>
      <li>marisavantry@plumwick.net</li>
      <li>www.marisavantrydesigns-example.com</li>
    </ul>
  </section>

</main>
</body>
</html>
```